Psychologist in Private Practice Needs a Website Update

Project Description:
Hello talented designers! My current website, www.jodelbrisk.com, needs a fresh, boho-modern makeover that highlights the warm, welcoming nature of my holistic therapy practice. I want a website that has a serene, boho- modern design, appealing to clients seeking individual therapy, couples therapy, and family counseling.

I’d also like to prepare for a future second site focused exclusively on couples and family therapy. Both sites should be interconnected, so I’m looking for design suggestions that seamlessly link them together while maintaining a cohesive brand look and feel.

Key Objectives:

Boho-Modern Aesthetic: Incorporate natural textures, neutral or earthy tones, and clean lines that capture a modern, inviting vibe.

Responsive Design: Ensure the website is user-friendly on desktop, tablet, and mobile devices.

Clear Service Offerings: Prominently feature my three distinct services: individual therapy, couples therapy, and family counseling.

Interlinked Future Site: Provide ideas on how to cross-link this site with a second site focused on couples and family therapy.

User Experience (UX): Make the site simple to navigate, with intuitive placement of content that speaks to potential clients’ needs.

SEO-Friendly: Implement best practices for structure, site speed, and keyword usage to boost online visibility.

What I Have Now:
Existing website: www.jodelbrisk.com
Basic content and a logo that can be refined or updated to match the boho-modern feel
Rough style guide with brand elements open to a fresh interpretation

Preferred Style/Tone:
Boho-modern with earthy tones, subtle textures, and clean typography
Warm, empathetic, and approachable to align with the nature of therapy services
Slightly artistic or organic elements that evoke calm and connection

Potential for an ongoing design relationship!
Updates

Need extra days to review

Target Market(s)

I have a high functioning, professional clientele who doctors, lawyers, and leaders in their field.

Industry/Entity Type

healthcare/mental health

Coding

Coded - Design and coding required

Font styles to use
Other font styles liked:
• cormorant garamond for headers and Source Sans Pro for supporting text

Colors

Designer to choose colors to be used in the design.

Requirements
Must have
• Open, Harmonious Layout I’d like the overall design to feel upscale, humanistic, open and harmonious, with minimal divisions of space. Rather than traditional section dividers, please consider using images, subtle shifts in color, typography, or spacing to define sections. Hero Image & Inspiration Ideally, the first (hero) image should evoke a sense of awe or inspiration. Focus on simplicity and elegance so the design feels spacious and inviting, allowing the content and imagery to really stand out. Natural Flow Wherever possible, let the design elements flow naturally into each other, creating a sense of unity and cohesion throughout the site.
Nice to have
• 1. Full-Width Hero Image: • The homepage should feature a full-width hero image that extends edge-to-edge across the screen for a modern and visually immersive effect. • This image should set the tone for the website, reflecting a calming, humanistic/natural, and upscale feel. It could include subtle overlays or gradients to enhance readability of text and navigation elements. Ideally, this image should have one or two people in nature. The image could be slightly transparent to allow the text "holistic therapy" and the tagline "an integrative approach to transformation" to be easily visible. Please help me find a breath-taking image that evokes a sense of beauty, inspiration, awe or hope. 2. Menu Tabs Positioned Over the Image: • The menu tabs (navigation bar) should be positioned directly on top of the hero image, either centered or aligned to the top right/left, depending on the design. • The navigation bar should have a slightly transparent or solid background (depending on the image and visibility needs) to ensure the text is easily readable without detracting from the image. 3. Typography and Text Placement: • The text overlay on the hero image should use the selected fonts: • Cormorant Garamond for headers (e.g., the tagline or welcome message). • Source Sans Pro for any supporting text. 5. Seamless Transitions: • Below the full-width image, transitions into the next sections (like “About,” “Services,” or client-focused content) should be smooth, using full-width separators that maintain the cohesive, open layout style. 6. Color Palette: • A neutral and calming color palette should be used (e.g., soft blues, grays, whites, or very muted earth tones) to create a soothing atmosphere for visitors. This design approach ensures the homepage looks clean, modern, and professional while maintaining the calming and upscale aesthetic that reflects the values of my psychology practice

```html
<!DOCTYPE html>
<html lang="en">
<head>
<meta charset="utf-8">
<title>Dr. Lena Marwood — Holistic Therapy</title>
<link rel="stylesheet" href="https://fonts.googleapis.com/css2?family=Raleway:wght@400;500;600&family=Montserrat:wght@400;500;600&display=swap">
<style>
:root{
  --gold:#e8b65a;
  --gold-soft:#f3ddb0;
  --ink:#1f1f1f;
  --text:#575757;
  --cream:#fcf5e8;
  --mist:#e6efec;
  --line:#e2cfa6;
  --white:#ffffff;
}
*{box-sizing:border-box;margin:0;padding:0}
html,body{width:1200px;height:5172px;overflow:hidden}
body{position:relative;font-family:"Montserrat",sans-serif;color:var(--text);background:var(--cream)}
.abs{position:absolute}
h1,h2,h3,.brand-name{font-family:"Raleway",sans-serif;color:var(--ink);font-weight:500}
.btn{position:absolute;display:flex;align-items:center;justify-content:center;background:var(--gold);color:var(--white);font-size:17px;font-weight:600;letter-spacing:.5px;text-transform:uppercase;text-decoration:none}
p{font-size:15.5px;line-height:26.5px}

/* header */
.brand{left:110px;top:28px;line-height:1}
.brand-name{font-size:33px;font-weight:400;display:block}
.brand-role{font-family:"Raleway",sans-serif;font-size:25px;color:var(--ink);display:block;margin-top:4px}
.topbar{right:112px;top:25px;font-size:16px;color:var(--ink);display:flex;gap:16px;align-items:center}
.topbar svg{width:15px;height:15px;fill:var(--gold);vertical-align:-2px;margin-right:6px}
.nav{right:112px;top:68px;display:flex;gap:38px;font-size:17px;color:var(--ink)}
.nav .active{color:var(--gold)}

/* hero */
.hero{left:0;top:0;width:1200px;height:730px;background:linear-gradient(180deg,#f4e7c8 0%,#f5d99a 30%,#f0c676 48%,#e8c48c 62%,#d8cfc2 80%,var(--cream) 100%)}
.hero-glow{left:360px;top:320px;width:420px;height:420px;border-radius:50%;background:radial-gradient(circle,#fff6d8 0%,rgba(255,240,200,.5) 35%,rgba(255,240,200,0) 70%)}
.hero-figure{left:590px;top:170px;width:420px;height:520px;background:linear-gradient(180deg,rgba(120,90,60,.15),rgba(250,250,250,.55) 40%,rgba(235,235,235,.6));border-radius:200px 200px 40px 40px}
.hero h1{left:106px;top:232px;font-size:68px;font-weight:500}
.hero .tagline{left:111px;top:338px;font-size:21px;color:var(--ink)}
.social{left:1140px;display:flex;flex-direction:column;gap:10px;top:418px}
.social span{width:44px;height:44px;border-radius:50%;background:#3a3a3a;display:block}

/* about */
.about{left:0;top:730px;width:1200px;height:640px;background:var(--cream)}
.arch{left:110px;top:20px;width:436px;height:584px;background:var(--gold-soft);border-radius:218px 218px 0 0;opacity:.7}
.arch-photo{left:132px;top:46px;width:392px;height:534px;border-radius:196px 196px 0 0;background:linear-gradient(160deg,#d8d3cc 0%,#b9a48b 35%,#2a2523 60%,#1c1a19 100%)}
.about h2{left:632px;top:68px;font-size:41px}
.about .lead{left:633px;top:134px;width:460px;font-size:21px;line-height:30px;color:var(--gold)}
.about .intro{left:633px;top:212px;width:460px}
.checks{left:633px;top:346px;list-style:none;font-size:16px;color:var(--ink)}
.checks li{height:29px;display:flex;align-items:center;gap:10px}
.checks svg{width:14px;height:14px;stroke:var(--gold);fill:none;stroke-width:3}

/* services */
.services{left:0;top:1370px;width:1200px;height:1850px;background:linear-gradient(180deg,var(--cream) 0%,var(--mist) 12%,#eef2ea 50%,#f6eedd 80%,#ead9c2 92%,var(--cream) 100%)}
.services h2{left:0;width:1200px;text-align:center;top:164px;font-size:41px}
.service h3{font-size:30px}
.service .sub{font-size:14.5px;line-height:26px;color:var(--ink)}
.circle{width:448px;height:448px;border-radius:50%}
.c1{left:656px;top:256px;background:linear-gradient(180deg,#efe6da 0%,#dcd6ce 45%,#b7b3aa 60%,#e5dccd 100%)}
.c2{left:92px;top:740px;background:linear-gradient(160deg,#f2c7b2 0%,#e4c7ad 40%,#9aa3a6 75%,#7b8687 100%)}
.c3{left:656px;top:1256px;background:linear-gradient(180deg,#8d8c8a 0%,#a69685 40%,#c9a777 70%,#b08b5a 100%)}

/* faq */
.faq{left:0;top:3220px;width:1200px;height:810px;background:var(--cream)}
.faq h2{left:0;width:1200px;text-align:center;top:50px;font-size:44px}
.faq-list{left:198px;top:124px;width:800px}
.faq-item{border-bottom:2px solid var(--line);height:68px;display:flex;align-items:center;justify-content:space-between;padding:0 12px;font-size:18px;font-weight:500;color:var(--ink)}
.faq-item.open{color:var(--gold);height:62px;border-bottom-color:var(--gold-soft)}
.faq-item svg{width:12px;height:12px;stroke:var(--ink);fill:none;stroke-width:2}
.faq-answer{padding:20px 12px 18px;border-bottom:2px solid var(--line);font-size:15px;line-height:23px;color:var(--ink)}
.faq-answer p{font-size:15px;line-height:23px}

/* partnership */
.partner{left:0;top:4030px;width:1200px;height:730px;background:linear-gradient(180deg,var(--cream) 0%,#f6d7a2 8%,#eec07c 12%,#d9b894 20%,#b8a99a 45%,#c9c0b6 75%,#ece6dc 92%,var(--cream) 100%)}
.partner-card{left:110px;top:120px;width:976px;height:492px;background:var(--white)}
.partner-photo{left:0;top:0;width:396px;height:492px;background:linear-gradient(180deg,#f3d396 0%,#d79a49 35%,#8a5a2a 70%,#4a3220 100%)}
.partner-card h2{left:450px;top:44px;font-size:43px}
.partner-card p{position:absolute;left:452px;top:126px;width:470px}

/* footer */
.footer{left:0;top:4760px;width:1200px;height:412px;background:var(--cream)}
.footer .brand{top:88px}
.footer .brand-name{font-size:38px}
.footer .brand-role{font-size:29px}
.fcol{top:50px}
.fcol h4{font-family:"Montserrat",sans-serif;font-weight:500;font-size:19px;color:var(--ink);margin-bottom:14px}
.fcol ul{list-style:none;font-size:15.5px;color:var(--ink)}
.fcol li{height:31px}
.fcol svg{width:14px;height:14px;fill:var(--gold);vertical-align:-2px;margin-right:8px}
.rule{left:110px;top:300px;width:978px;height:1px;background:#cfc6b6}
.copy{left:0;width:1200px;top:336px;text-align:center;font-size:15px;color:var(--ink)}
</style>
</head>
<body>

<section class="abs hero">
  <div class="abs hero-glow"></div>
  <div class="abs hero-figure" role="img" aria-label="Woman meditating cross-legged on a hilltop facing a sunrise over the sea"></div>
  <h1 class="abs">Holistic Therapy</h1>
  <div class="abs tagline">An integrative approach to transformation</div>
  <a class="btn" style="left:110px;top:413px;width:358px;height:60px" href="#">Couples and Family Therapy</a>
</section>

<header>
  <div class="abs brand"><span class="brand-name">Dr. Lena Marwood</span><span class="brand-role">Licensed Psychologist</span></div>
  <div class="abs topbar">
    <span><svg viewBox="0 0 24 24"><path d="M6.6 10.8c1.4 2.8 3.8 5.1 6.6 6.6l2.2-2.2c.3-.3.7-.4 1-.2 1.1.4 2.3.6 3.6.6.6 0 1 .4 1 1V20c0 .6-.4 1-1 1C10.6 21 3 13.4 3 4c0-.6.4-1 1-1h3.5c.6 0 1 .4 1 1 0 1.3.2 2.5.6 3.6.1.3 0 .7-.2 1z"/></svg>(555) 214-7730</span>
    <span>|</span>
    <span><svg viewBox="0 0 24 24"><path d="M2 5h20v14H2z"/></svg>hello@lenamarwood.com</span>
  </div>
  <nav class="abs nav"><span class="active">Home</span><span>Services</span><span>About</span><span>Faqs</span><span>Blog</span><span>Contact</span></nav>
</header>

<div class="abs social" aria-label="Social links"><span></span><span></span><span></span></div>

<section class="abs about">
  <div class="abs arch"></div>
  <div class="abs arch-photo" role="img" aria-label="Portrait of the psychologist smiling in a bright room"></div>
  <h2 class="abs">Dr. Lena Marwood</h2>
  <p class="abs lead">Are you struggling with issues that affect the way you live, love or work?</p>
  <p class="abs intro">Dr. Lena Marwood and her associates are licensed psychologists in Towson, Maryland. We offer therapy for individuals, couples and families to help you create meaningful change, whether you:</p>
  <ul class="abs checks">
    <li><svg viewBox="0 0 16 16"><path d="M2 8l4 4 8-8"/></svg>Feel overwhelmed with depression or anxiety.</li>
    <li><svg viewBox="0 0 16 16"><path d="M2 8l4 4 8-8"/></svg>Experience a lack of connection in your marriage.</li>
    <li><svg viewBox="0 0 16 16"><path d="M2 8l4 4 8-8"/></svg>Worry excessively about what others think.</li>
    <li><svg viewBox="0 0 16 16"><path d="M2 8l4 4 8-8"/></svg>Have a history of trauma or abuse.</li>
    <li><svg viewBox="0 0 16 16"><path d="M2 8l4 4 8-8"/></svg>Parent a child with complex needs.</li>
    <li><svg viewBox="0 0 16 16"><path d="M2 8l4 4 8-8"/></svg>Struggle with other life challenges.</li>
  </ul>
  <a class="btn" style="left:633px;top:550px;width:150px;height:58px" href="#">Read More</a>
</section>

<section class="abs services">
  <h2 class="abs">What We Do</h2>

  <article class="service">
    <h3 class="abs" style="left:108px;top:296px">Individual Therapy</h3>
    <p class="abs sub" style="left:110px;top:352px;width:420px">Offering therapy online or in the office conveniently located in towson, maryland</p>
    <p class="abs" style="left:110px;top:432px;width:478px">We work with adults (age 18+) using a highly personalized and flexible approach tailored to each client's individual needs. Dr. Lena Marwood and her associates are attuned to contextual issues including, but not limited to, ethnic or racial identity, sexual identity, nationality, and family culture and tradition.</p>
    <a class="btn" style="left:110px;top:622px;width:150px;height:58px" href="#">Read More</a>
    <div class="abs circle c1" role="img" aria-label="Man meditating on a beach at sunset"></div>
  </article>

  <article class="service">
    <div class="abs circle c2" role="img" aria-label="Smiling couple embracing by the sea"></div>
    <h3 class="abs" style="left:610px;top:782px">Couples Therapy</h3>
    <p class="abs sub" style="left:612px;top:838px;width:470px">Online and in-person marriage therapy &amp; family counseling located in baltimore county, maryland</p>
    <p class="abs" style="left:612px;top:916px;width:480px">Relationships are the heart of the human experience. Instead of giving couples and families advice, we help them to look underneath anger, frustration, and conflict to access their desires to feel connected and accepted by one another. We have specialized training in marriage and family therapy using Emotionally Focused Therapy (EFT) and Emotionally Focused Therapy for Families (EFFT).</p>
    <a class="btn" style="left:612px;top:1132px;width:150px;height:58px" href="#">Read More</a>
  </article>

  <article class="service">
    <h3 class="abs" style="left:108px;top:1296px">Family Counseling</h3>
    <p class="abs sub" style="left:110px;top:1352px;width:470px">Online and in-person marriage therapy &amp; family counseling located in baltimore county, maryland</p>
    <p class="abs" style="left:110px;top:1430px;width:480px">Relationships are the heart of the human experience. Instead of giving couples and families advice, we help them to look underneath anger, frustration, and conflict to access their desires to feel connected and accepted by one another. We have specialized training in marriage and family therapy using Emotionally Focused Therapy (EFT) and Emotionally Focused Therapy for Families (EFFT).</p>
    <a class="btn" style="left:110px;top:1654px;width:150px;height:58px" href="#">Read More</a>
    <div class="abs circle c3" role="img" aria-label="Family walking through an autumn meadow with a child in a yellow coat"></div>
  </article>
</section>

<section class="abs faq">
  <h2 class="abs">Frequently Asked Questions</h2>
  <div class="abs faq-list">
    <div class="faq-item open">Where are you located?<svg viewBox="0 0 12 12"><path d="M2 8l4-4 4 4"/></svg></div>
    <div class="faq-answer">
      <p>Our clinicians hold both virtual and in person sessions. Virtual sessions are held via Hearthlink.</p>
      <p style="margin-top:23px">In person sessions are held out of our office location at 418 Linden Hollow Road, Towson MD 21204. The home office has a separate entrance. You should walk up the front walkway toward the porch, bear left and follow the path along the side of the house. Just before you reach the gate, you will see stairs leading down to the waiting room entrance.</p>
    </div>
    <div class="faq-item">What states do you offer telehealth in?<svg viewBox="0 0 12 12"><path d="M2 4l4 4 4-4"/></svg></div>
    <div class="faq-item">What types of clients do you see?<svg viewBox="0 0 12 12"><path d="M2 4l4 4 4-4"/></svg></div>
    <div class="faq-item">Do you take insurance?<svg viewBox="0 0 12 12"><path d="M2 4l4 4 4-4"/></svg></div>
    <div class="faq-item">How do out of network benefits work?<svg viewBox="0 0 12 12"><path d="M2 4l4 4 4-4"/></svg></div>
  </div>
  <a class="btn" style="left:525px;top:700px;width:150px;height:58px" href="#">View More</a>
</section>

<section class="abs partner">
  <div class="abs partner-card">
    <div class="abs partner-photo" role="img" aria-label="Woman raising joined hands toward a golden mountain sunset"></div>
    <h2 class="abs">Therapy is a Partnership</h2>
    <p>Our clinicians utilize contemporary neuroscience-informed therapies along with the wisdom of traditional psychotherapy to foster insight, mindfulness, self-compassion, and deeper connections to oneself and others. Together, in a safe and non-judgmental environment, we will work to understand what holds you back from living the life you really want. All are welcome and celebrated.</p>
    <a class="btn" style="left:452px;top:380px;width:286px;height:58px" href="#">Make an Appointment</a>
  </div>
</section>

<footer class="abs footer">
  <div class="abs brand"><span class="brand-name">Dr. Lena Marwood</span><span class="brand-role">Licensed Psychologist</span></div>
  <div class="abs fcol" style="left:504px">
    <h4>Quick links</h4>
    <ul><li>Home</li><li>Services</li><li>About</li><li>Faqs</li><li>Blog</li><li>Contact</li></ul>
  </div>
  <div class="abs fcol" style="left:694px">
    <h4>Contact information</h4>
    <ul>
      <li style="height:62px"><svg viewBox="0 0 24 24"><path d="M6.6 10.8c1.4 2.8 3.8 5.1 6.6 6.6l2.2-2.2c.3-.3.7-.4 1-.2 1.1.4 2.3.6 3.6.6.6 0 1 .4 1 1V20c0 .6-.4 1-1 1C10.6 21 3 13.4 3 4c0-.6.4-1 1-1h3.5c.6 0 1 .4 1 1 0 1.3.2 2.5.6 3.6.1.3 0 .7-.2 1z"/></svg>Call (555) 214-7730</li>
      <li><svg viewBox="0 0 24 24"><path d="M2 5h20v14H2z"/></svg>Email hello@lenamarwood.com</li>
    </ul>
  </div>
  <div class="abs rule"></div>
  <div class="abs copy">©2025, Lena Marwood. All Rights Reserved.</div>
</footer>

</body>
</html>
```